Tin Gull Wick Co. 3x3x3 reverse tuck product box

Coconut wax candles in paint cans. Fun, unpretentious. Every label has a different design that reflects the candle scent. Eclectic but simple branding. I want to take a minimalist approach as I need one box design to work for all of my product. Since my candles are so colorful and unique, I like Black and white (like my logo) on Kraft background. No candle names on the box, just my logo and welcome message on the back of the box with pertinent info (see "must haves"). Need to reflect my brand in one box that will work with my many unique labels. Company logo is black & white. I need to fit a particular template for printing. I really like the idea of a kraft background, but it would need to be a vector as my printing company cannot print white ink on kraft boxes. I am very open to non-kraft related art if it looks great! Please see requirement document. I have uploaded some of my product so the general feel of the brand is available. One candle per box. My website is www.tingullwick.com. My website and marketing material is minimalist since my each of my products are very unique and busy. Feel free to read my product descriptions to get a feel for my brand.

Target Market(s)

18-45 year olds

Industry/Entity Type

Candles/gifts

Font styles to use
Other font styles liked:
• NOW

Colors

Designer to choose colors to be used in the design.

Requirements
Must have
• My business logo, cruelty free logo, Paraben-free logo, recyclable , and handmade in Austin, TX
Nice to have
• I've uploaded a pic with back of box text I would like to see. My company tagline is: Coconut Wax Candle Awesomeness.
Should not have
• My candle label art on the box. I have many unique labels, and I will need this box to work for all of them.

```html
<!DOCTYPE html>
<html lang="en">
<head>
<meta charset="utf-8">
<title>Tin Gull Wick Co. – 3x3x3 Reverse Tuck Box Panels</title>
<link rel="stylesheet" href="https://fonts.googleapis.com/css2?family=Oswald:wght@400;600&family=Jost:wght@400&display=swap">
<style>
  :root {
    --bg: #e4e4e4;
    --kraft: #c9a47a;
    --kraft-edge: #b8926a;
    --ink: #111111;
  }
  * { box-sizing: border-box; margin: 0; padding: 0; }
  html, body { width: 1200px; height: 977px; overflow: hidden; }
  body {
    background: var(--bg);
    display: flex;
    align-items: center;
    justify-content: center;
    gap: 30px;
    color: var(--ink);
  }
  .panel {
    width: 360px;
    height: 360px;
    background: var(--kraft);
    border: 1px solid var(--kraft-edge);
    position: relative;
  }

  /* Back panel */
  .panel--back { padding: 22px 22px 18px; display: flex; flex-direction: column; }
  .origin {
    display: flex; align-items: center; justify-content: space-between;
    font-family: "Oswald", sans-serif; font-weight: 600;
    font-size: 13px; letter-spacing: 0.3px; text-transform: uppercase;
  }
  .origin__map { width: 40px; height: 40px; background: var(--ink); border-radius: 4px 10px 14px 6px; }
  .welcome {
    margin-top: 8px;
    border: 1.5px solid var(--ink);
    padding: 12px 10px;
    font-family: "Oswald", sans-serif; font-weight: 400;
    font-size: 19px; line-height: 1.2; text-align: center; text-transform: uppercase;
  }
  .badges { margin-top: auto; display: flex; align-items: center; gap: 22px; }
  .badge { background: none; border: 1.5px solid var(--ink); }
  .badge--recycle { width: 40px; height: 40px; border-radius: 50%; }
  .badge--cruelty { width: 50px; height: 36px; border-radius: 18px; }
  .badge--paraben { width: 92px; height: 44px; border-radius: 6px; }

  /* Front panel */
  .panel--front { display: flex; flex-direction: column; align-items: center; justify-content: center; gap: 18px; }
  .brand {
    display: flex; align-items: center; gap: 10px;
    font-family: "Jost", sans-serif; font-weight: 400; font-size: 30px;
  }
  .brand__mark { width: 14px; height: 14px; border: 1.5px solid var(--ink); }
  .tagline { font-family: "Jost", sans-serif; font-size: 15px; }

  /* Top panel */
  .panel--top { display: flex; align-items: center; justify-content: center; }
  .panel--top .brand { font-size: 22px; }
</style>
</head>
<body>
  <section class="panel panel--back" aria-label="Back panel">
    <div class="origin">
      <span>Handmade in</span>
      <div class="origin__map" role="img" aria-label="Silhouette map of Texas"></div>
      <span>Austin, TX Y'all</span>
    </div>
    <p class="welcome">Hi, I'm your awesome new Tin Gull Wick candle. You obviously have excellent taste and a great sense of humor. Keep it up the world needs more people like you.</p>
    <div class="badges">
      <div class="badge badge--recycle" role="img" aria-label="Recyclable badge"></div>
      <div class="badge badge--cruelty" role="img" aria-label="Cruelty free badge"></div>
      <div class="badge badge--paraben" role="img" aria-label="Paraben free badge"></div>
    </div>
  </section>

  <section class="panel panel--front" aria-label="Front panel">
    <div class="brand"><span class="brand__mark"></span><span>Tin Gull Wick Co.</span></div>
    <p class="tagline">Coconut Wax Candle Awesomeness</p>
  </section>

  <section class="panel panel--top" aria-label="Top panel">
    <div class="brand"><span class="brand__mark"></span><span>Tin Gull Wick Co.</span></div>
  </section>
</body>
</html>
```